Business Consulting Company needs a business card designed

We need a business card in Brisbane Australia for a company called " Marrowvale Consulting Group". I would like to see the designs either in purple or green color

```html
<!DOCTYPE html>
<html lang="en">
<head>
<meta charset="utf-8">
<title>Marrowvale Consulting Group – Business Card</title>
<link rel="stylesheet" href="https://fonts.googleapis.com/css2?family=Michroma&display=swap">
<style>
  :root {
    --backdrop: #cccbd3;
    --card-white: #f8f7f9;
    --card-shade: #e5e3e8;
    --brand-purple: #6a3a9c;
    --band-deep: #4e2378;
    --band-light: #8f5cc6;
    --swoosh-dark: #4a4852;
    --swoosh-light: #a9a6b0;
    --name-ink: #4b2a7e;
    --title-ink: #4a4852;
    --contact-ink: #ffffff;
  }
  html, body {
    margin: 0;
    padding: 0;
    width: 1200px;
    height: 887px;
    overflow: hidden;
    background: var(--backdrop);
    font-family: "Michroma", "Eurostile", sans-serif;
  }
  .business-card {
    position: absolute;
    left: 80px;
    top: 146px;
    width: 1040px;
    height: 594px;
    background: radial-gradient(ellipse at 50% 35%, var(--card-white) 0%, var(--card-shade) 100%);
    box-shadow: 0 18px 40px rgba(0,0,0,0.22);
    overflow: hidden;
  }
  .card-graphics {
    position: absolute;
    inset: 0;
  }
  .brand {
    position: absolute;
    left: 90px;
    top: 60px;
    width: 420px;
    text-align: center;
    color: var(--brand-purple);
  }
  .brand-dot {
    display: block;
    width: 64px;
    height: 64px;
    margin: 0 auto 22px;
    border-radius: 50%;
    background: var(--brand-purple);
  }
  .brand-name {
    margin: 0;
    font-size: 24px;
    font-weight: 400;
    line-height: 1.45;
    letter-spacing: 1px;
  }
  .holder {
    position: absolute;
    right: 70px;
    top: 292px;
    text-align: right;
  }
  .holder-name {
    margin: 0;
    font-size: 21px;
    font-weight: 400;
    letter-spacing: 3px;
    color: var(--name-ink);
  }
  .holder-title {
    margin: 8px 0 0;
    font-size: 14px;
    letter-spacing: 2.5px;
    font-variant: small-caps;
    color: var(--title-ink);
  }
  .contacts {
    position: absolute;
    left: 0;
    right: 0;
    top: 432px;
    color: var(--contact-ink);
    font-size: 14px;
    letter-spacing: 1.6px;
    font-variant: small-caps;
  }
  .contact-row {
    display: flex;
    justify-content: center;
    align-items: center;
    gap: 18px;
    margin-bottom: 18px;
  }
  .contact-item {
    display: inline-flex;
    align-items: center;
    gap: 7px;
    white-space: nowrap;
  }
  .contact-icon {
    width: 15px;
    height: 15px;
    flex: none;
  }
</style>
</head>
<body>
  <article class="business-card">
    <svg class="card-graphics" viewBox="0 0 1040 594" width="1040" height="594" aria-hidden="true">
      <defs>
        <linearGradient id="band-fill" x1="0" x2="1" y1="0" y2="0">
          <stop offset="0" stop-color="var(--band-deep)"/>
          <stop offset="0.45" stop-color="var(--band-light)"/>
          <stop offset="1" stop-color="var(--band-deep)"/>
        </linearGradient>
        <linearGradient id="swoosh-fill" x1="0" x2="1" y1="0" y2="0">
          <stop offset="0" stop-color="var(--swoosh-dark)"/>
          <stop offset="0.55" stop-color="var(--swoosh-light)"/>
          <stop offset="1" stop-color="var(--swoosh-dark)"/>
        </linearGradient>
      </defs>
      <path class="swoosh" fill="url(#swoosh-fill)"
        d="M0,262 C250,318 450,342 620,345 C800,348 950,368 1040,402
           L1040,408 C950,380 800,362 620,360 C450,358 250,336 0,272 Z"/>
      <path class="purple-band" fill="url(#band-fill)"
        d="M0,290 C250,340 450,366 620,368 C800,370 950,390 1040,416 L1040,594 L0,594 Z"/>
    </svg>

    <div class="brand">
      <span class="brand-dot"></span>
      <p class="brand-name">Marrowvale Consulting<br>Group</p>
    </div>

    <div class="holder">
      <p class="holder-name">DANIEL WHITFORD</p>
      <p class="holder-title">Managing Director</p>
    </div>

    <div class="contacts">
      <div class="contact-row">
        <span class="contact-item">
          <svg class="contact-icon" viewBox="0 0 16 16"><circle cx="8" cy="8" r="7.5" fill="#fff"/><path d="M8 3.5a3 3 0 0 0-3 3c0 2.2 3 6 3 6s3-3.8 3-6a3 3 0 0 0-3-3z" fill="var(--band-light)"/></svg>
          Suite # 118, Kell Bldg, Brisbane QLD 4000
        </span>
        <span class="contact-item">
          <svg class="contact-icon" viewBox="0 0 16 16"><circle cx="8" cy="8" r="7.5" fill="#fff"/><g fill="none" stroke="var(--band-light)" stroke-width="1.1"><circle cx="8" cy="8" r="5"/><ellipse cx="8" cy="8" rx="2.2" ry="5"/><path d="M3 8h10"/></g></svg>
          www.Marrowvalecg.com.au
        </span>
      </div>
      <div class="contact-row">
        <span class="contact-item">
          <svg class="contact-icon" viewBox="0 0 16 16"><circle cx="8" cy="8" r="7.5" fill="#fff"/><path d="M5 4.5l1.8-.5 1 2.3-1 .8a5 5 0 0 0 2.1 2.1l.8-1 2.3 1-.5 1.8C8 11 5 8 5 4.5z" fill="var(--band-light)"/></svg>
          07 3555 0142
        </span>
        <span class="contact-item">
          <svg class="contact-icon" viewBox="0 0 16 16"><circle cx="8" cy="8" r="7.5" fill="#fff"/><rect x="5.5" y="3.5" width="5" height="9" rx="1" fill="var(--band-light)"/></svg>
          0491 570 156
        </span>
        <span class="contact-item">
          <svg class="contact-icon" viewBox="0 0 16 16"><circle cx="8" cy="8" r="7.5" fill="#fff"/><rect x="4" y="6" width="8" height="6" fill="var(--band-light)"/><rect x="5.5" y="3.5" width="5" height="3" fill="var(--band-light)"/></svg>
          07 3555 0198
        </span>
        <span class="contact-item">
          <svg class="contact-icon" viewBox="0 0 16 16"><circle cx="8" cy="8" r="7.5" fill="#fff"/><rect x="3.5" y="5" width="9" height="6" fill="var(--band-light)"/><path d="M3.5 5l4.5 3.5L12.5 5" fill="none" stroke="#fff" stroke-width="0.9"/></svg>
          info@Marrowvalecg.com.au
        </span>
      </div>
    </div>
  </article>
</body>
</html>
```